Online Art Gallery & Art Management Firm looking for a business card

I'm launching an online art gallery (paintings, photography, drawings, furniture, books, ...) where people can buy all types of art. It's a platform where young and unknown artists can showcase their oeuvre.

Additionally, the venture will act as my advising company for artists. I help them out with their business side of life and become their representative.

The company name: The Velmora House
Logo is attached

I'm looking for something very classy and upmarket.
Updates

Reason: Logo wasn't finished yet...

The design should include the following information: - Name: Pieter Drovensky - Title: Founder - Mobile: +32 (0) 485 613 204 - E-mail: pieter@velmora-house.net - Website www.velmora-house.net I prefer the have the logo (without website) on the one side and the information on the other. Best regards Pieter

Target Market(s)

Art buyers / art dealers / artists / middle class / upmarket /

Industry/Entity Type

Artists

Colors

Designer to choose colors to be used in the design.

Requirements
Must have
• Must communicate credibility, trust and integrity
Nice to have
• Something classy, chique
Should not have
• Nothing to artistic or creative

```html
<!DOCTYPE html>
<html lang="en">
<head>
<meta charset="utf-8">
<title>The Velmora House — Business Card</title>
<link rel="stylesheet" href="https://fonts.googleapis.com/css2?family=Josefin+Sans:wght@200&display=swap">
<style>
  :root {
    --page: #ffffff;
    --card: #ffffff;
    --card-edge: #f6e3cf;
    --amber: #d98427;
    --ink: #6b3a12;
  }
  html, body {
    margin: 0;
    padding: 0;
    width: 1200px;
    height: 785px;
    overflow: hidden;
    background: var(--page);
  }
  .canvas {
    position: relative;
    width: 1200px;
    height: 785px;
  }
  .card {
    position: absolute;
    left: 132px;
    top: 132px;
    width: 936px;
    height: 521px;
    background: var(--card);
    box-shadow: inset 0 0 0 1px var(--card-edge);
    overflow: hidden;
  }
  .card__sweep {
    position: absolute;
    inset: 0;
    width: 100%;
    height: 100%;
  }
  .card__sweep path { fill: var(--amber); }
  .wordmark {
    position: absolute;
    left: 0;
    right: 0;
    top: 226px;
    margin: 0;
    text-align: center;
    font-family: "Josefin Sans", sans-serif;
    font-weight: 200;
    font-size: 40px;
    line-height: 1;
    letter-spacing: 0.22em;
    text-transform: uppercase;
    color: var(--ink);
    padding-left: 0.22em;
  }
  .wordmark__rule {
    position: absolute;
    left: 168px;
    top: 310px;
    width: 609px;
    height: 2px;
  }
  .wordmark__rule line {
    stroke: var(--ink);
    stroke-width: 2;
    stroke-dasharray: 9 6;
  }
</style>
</head>
<body>
  <main class="canvas">
    <section class="card" aria-label="Business card, front">
      <svg class="card__sweep" viewBox="0 0 936 521" preserveAspectRatio="none" aria-hidden="true">
        <path d="M0 0 H936 Q568 288 0 521 Z"/>
      </svg>
      <h1 class="wordmark">The Velmora House</h1>
      <svg class="wordmark__rule" viewBox="0 0 609 2" aria-hidden="true">
        <line x1="0" y1="1" x2="609" y2="1"/>
      </svg>
    </section>
  </main>
</body>
</html>
```